National Sales & Merchandising Company Needs a PowerPoint design

We need a professional PowerPoint template designed for our Sydney based National Sales & Merchandising Company. We provide sales representatives and merchandisers to companies working in the FMCG space, such as Fizzmont, Larkwells, Dorvan's, Kelmor (Vitalux Pop N Sip) and Brulo (Morning Press). We would like someone to use the colours/ design elements from our website (www.brightlanereps.com.au). We require a couple of different PPT templates with white backgrounds (e.g. first slide, new section slide, using an interesting new bullet point style, table and chart friendly and with space for headers and footers. We want a clean but dynamic look.
Reason: Hi designers,
Hoping to see some fluid lines around the outside of the slides, not coloured boxes that I could create myself. White background is required too.
Please see our website for ideas.
Thanks,
Mira
It Company

```html
<!DOCTYPE html>
<html lang="en">
<head>
<meta charset="utf-8">
<title>Content/Graph Slide</title>
<link rel="stylesheet" href="https://fonts.googleapis.com/css2?family=Archivo+Black&family=Carlito:wght@400;700&display=swap">
<style>
  :root {
    --navy: #1f3563;
    --gold: #f5b800;
    --gold-soft: #f7c948;
    --white: #ffffff;
    --photo-deep: #1b2f6b;
    --photo-amber: #e8a21c;
    --photo-orange: #c9700f;
  }
  html, body {
    margin: 0;
    padding: 0;
    overflow: hidden;
    background: var(--white);
  }
  .slide {
    position: relative;
    width: 1200px;
    height: 901px;
    background: var(--white);
    overflow: hidden;
    font-family: "Carlito", "Calibri", sans-serif;
    color: var(--navy);
  }
  .slide-title {
    position: absolute;
    left: 20px;
    top: 170px;
    margin: 0;
    font-family: "Archivo Black", "Arial Black", sans-serif;
    font-size: 70px;
    line-height: 1;
    letter-spacing: 0;
    color: var(--navy);
    white-space: nowrap;
  }
  .title-rule {
    position: absolute;
    left: 12px;
    top: 250px;
  }
  .column {
    position: absolute;
    top: 367px;
    width: 480px;
  }
  .column--one { left: 20px; }
  .column--two { left: 546px; }
  .column-heading {
    margin: 0 0 14px;
    font-size: 31px;
    font-weight: 700;
    line-height: 1.2;
  }
  .bullet-list {
    list-style: none;
    margin: 0;
    padding: 0;
  }
  .bullet-list li {
    position: relative;
    padding-left: 30px;
    font-size: 38px;
    line-height: 66px;
  }
  .bullet-list li::before {
    content: "";
    position: absolute;
    left: 2px;
    top: 31px;
    width: 9px;
    height: 9px;
    border: 2px solid var(--gold);
    background: var(--white);
    box-shadow: 2px 2px 0 var(--gold-soft);
  }
  .column-note {
    position: absolute;
    top: 390px;
    left: 0;
    margin: 0;
    font-size: 38px;
    line-height: 1.2;
    white-space: nowrap;
  }
  .photo-strip {
    position: absolute;
    top: 0;
    right: 0;
    width: 155px;
    height: 901px;
    background:
      linear-gradient(180deg,
        var(--photo-deep) 0%,
        #3a3f7a 8%,
        #f0b23a 22%,
        #2c3f86 30%,
        #f5d56a 40%,
        #e45f1a 48%,
        #ffe27a 55%,
        #f2b52b 66%,
        var(--photo-amber) 80%,
        var(--photo-orange) 100%);
  }
</style>
</head>
<body>
  <main class="slide">
    <h1 class="slide-title">Content/Graph Slide</h1>
    <svg class="title-rule" width="766" height="12" viewBox="0 0 766 12" aria-hidden="true">
      <path d="M0 10 Q380 2 766 5" fill="none" stroke="var(--gold)" stroke-width="2.5" stroke-linecap="round"/>
    </svg>

    <section class="column column--one">
      <h2 class="column-heading">Item ONE</h2>
      <ul class="bullet-list">
        <li>Bullet point one</li>
        <li>Bullet point two</li>
        <li>Bullet point three</li>
      </ul>
      <p class="column-note">Type more text here.</p>
    </section>

    <section class="column column--two">
      <h2 class="column-heading">Item TWO</h2>
      <ul class="bullet-list">
        <li>Bullet point one</li>
        <li>Bullet point two</li>
        <li>Bullet point three</li>
      </ul>
      <p class="column-note">Type more text here.</p>
    </section>

    <div class="photo-strip" role="img" aria-label="Long-exposure photograph of golden and orange light trails streaking against a deep blue night"></div>
  </main>
</body>
</html>
```